Business Cards for a Dating Coach/Social Dynamics company
Velvet Compass
Professional
Ted
Dating Instructor
4872 Marlow Terrace, #9
Coral Harbor, FL 33480
Skyheron@velvetcompasslife.com
www.velvetcompasslife.com

```html
<!DOCTYPE html>
<html lang="en">
<head>
<meta charset="utf-8">
<title>Velvet Compass – Business Cards</title>
<link href="https://fonts.googleapis.com/css2?family=Open+Sans:wght@400;600;700&display=swap" rel="stylesheet">
<style>
  :root {
    --canvas-bg: #d9d9d9;
    --card-grey: #4b4b4d;
    --card-grey-dark: #3f3f41;
    --accent-orange: #f07d1a;
    --accent-red: #d9361f;
    --band-light: #9a9a9c;
    --band-pale: #c4c4c6;
    --text-white: #ffffff;
    --text-soft: #e6e6e6;
  }
  * { margin: 0; padding: 0; box-sizing: border-box; }
  html, body {
    width: 1200px; height: 864px; overflow: hidden;
    background: var(--canvas-bg);
    font-family: "Open Sans", Arial, sans-serif;
  }
  .canvas {
    width: 1200px; height: 864px;
    display: flex; flex-direction: column; align-items: center; justify-content: center;
    gap: 36px;
  }
  .card {
    position: relative;
    width: 660px; height: 377px;
    border-radius: 26px;
    background: linear-gradient(160deg, var(--card-grey) 0%, var(--card-grey-dark) 100%);
    overflow: hidden;
    box-shadow: 0 6px 18px rgba(0,0,0,0.25);
  }

  /* Front */
  .card-front .brand {
    position: absolute; left: 0; right: 0; top: 130px;
    display: flex; align-items: center; justify-content: center; gap: 14px;
  }
  .brand-dot {
    width: 34px; height: 34px; border-radius: 50%;
    background: var(--accent-red);
  }
  .brand-name {
    font-weight: 600; font-size: 40px; color: var(--text-white);
    letter-spacing: 0.5px;
  }
  .card-front .front-web {
    position: absolute; left: 0; right: 0; top: 228px;
    text-align: center; color: var(--text-white);
    font-size: 17px; letter-spacing: 1.5px;
  }

  /* Back */
  .swoosh { position: absolute; left: 0; top: 0; }
  .back-brand {
    position: absolute; left: 60px; top: 70px;
    display: flex; align-items: center; gap: 12px;
  }
  .back-brand .brand-dot { width: 26px; height: 26px; }
  .back-brand .brand-name { font-size: 30px; }
  .tagline {
    position: absolute; left: 98px; top: 114px;
    font-size: 10.5px; font-weight: 600; letter-spacing: 1.6px;
    color: var(--text-soft); text-transform: uppercase;
  }
  .person {
    position: absolute; left: 98px; top: 150px;
  }
  .person-name { color: var(--accent-orange); font-weight: 700; font-size: 16px; }
  .person-role { color: var(--text-white); font-size: 13px; margin-top: 2px; }
  .address {
    position: absolute; left: 60px; top: 246px;
    color: var(--text-white); font-size: 13px; line-height: 1.55;
    font-style: normal;
  }
  .contacts {
    position: absolute; left: 338px; top: 150px;
    list-style: none; color: var(--text-white); font-size: 12.5px;
  }
  .contacts li { display: flex; align-items: center; gap: 10px; height: 25px; }
  .contact-icon {
    width: 17px; height: 17px; border-radius: 50%;
    background: var(--accent-red);
    display: flex; align-items: center; justify-content: center; flex: none;
  }
</style>
</head>
<body>
<main class="canvas">

  <section class="card card-front" aria-label="Card front">
    <div class="brand">
      <span class="brand-dot"></span>
      <span class="brand-name">Velvet Compass</span>
    </div>
    <p class="front-web">Velvetcompasslife.com</p>
  </section>

  <section class="card card-back" aria-label="Card back">
    <svg class="swoosh" width="660" height="377" viewBox="0 0 660 377">
      <path d="M0,360 C180,350 360,336 540,300 L540,312 C360,350 180,364 0,372 Z" fill="var(--accent-red)" opacity="0.9"/>
      <path d="M300,377 C470,350 590,300 660,200 L660,377 Z" fill="var(--band-pale)"/>
      <path d="M360,377 C500,350 610,300 660,240 L660,377 Z" fill="var(--band-light)"/>
      <path d="M240,377 C430,352 575,290 660,180 L660,198 C580,300 440,362 290,377 Z" fill="var(--accent-orange)"/>
      <path d="M440,377 C545,355 620,318 660,285 L660,377 Z" fill="var(--card-grey-dark)" opacity="0.55"/>
    </svg>

    <div class="back-brand">
      <span class="brand-dot"></span>
      <span class="brand-name">Velvet Compass</span>
    </div>
    <p class="tagline">Lifestyle and Dating Specialists</p>

    <div class="person">
      <p class="person-name">Ted</p>
      <p class="person-role">Dating Instructor</p>
    </div>

    <address class="address">
      4872 Marlow Terrace, #9<br>
      Coral Harbor, FL 33480
    </address>

    <ul class="contacts">
      <li>
        <span class="contact-icon">
          <svg width="9" height="9" viewBox="0 0 10 10"><path d="M2,1 L4,1 L4.6,3.2 L3.5,4 C4,5.2 4.8,6 6,6.5 L6.8,5.4 L9,6 L9,8 C9,8.6 8.6,9 8,9 C4.1,9 1,5.9 1,2 C1,1.4 1.4,1 2,1 Z" fill="#fff"/></svg>
        </span>
        555.014.2287
      </li>
      <li>
        <span class="contact-icon">
          <svg width="10" height="8" viewBox="0 0 10 8"><rect x="0.5" y="0.5" width="9" height="7" fill="none" stroke="#fff"/><path d="M0.5,0.5 L5,4.5 L9.5,0.5" fill="none" stroke="#fff"/></svg>
        </span>
        Skyheron@velvetcompasslife.com
      </li>
      <li>
        <span class="contact-icon">
          <svg width="10" height="10" viewBox="0 0 10 10"><circle cx="5" cy="5" r="4" fill="none" stroke="#fff"/><path d="M1,5 H9 M5,1 C3,3.5 3,6.5 5,9 C7,6.5 7,3.5 5,1" fill="none" stroke="#fff" stroke-width="0.8"/></svg>
        </span>
        www.velvetcompasslife.com
      </li>
    </ul>
  </section>

</main>
</body>
</html>
```